Crestline Lending Group Business Cards

We are looking to revamp the current business cards each of our locations uses. We are a lending company that specializes in personal loans, title loans, and tax services. We have locations in New Mexico, Texas, and Oklahoma.

We would like a cleaner, sleeker look while still highlighting what we offer. Title Loans, Personal Loans & Tax Services. We also want to include our referral fee somewhere on the card. We would like to see an English option as well as a Spanish option for the cards.

PLEASE NOTE: Some business cards do not include the employee's name but just the store's location, while others will include both.

These are double-sided business cards, and we would like to see proof if possible. I have included proofs of our current business cards for you to review below, as well as our company logo. Feel free to get creative with the logo, etc! Colors should match the logo; however, you do not need to use all of our logo colors if you don't want to.

```html
<!DOCTYPE html>
<html lang="en">
<head>
<meta charset="utf-8">
<title>Crestline Lending Group – Business Cards</title>
<link rel="stylesheet" href="https://fonts.googleapis.com/css2?family=Arimo:wght@400;700&family=Rubik+Dirt&display=swap">
<style>
  :root {
    --red: #c41f26;
    --green: #0e5a2e;
    --green-dark: #0b4a26;
    --grey-text: #7a7a7a;
    --white: #ffffff;
    --backdrop: #e6e6e6;
  }
  html, body {
    margin: 0;
    padding: 0;
    width: 1200px;
    height: 960px;
    overflow: hidden;
    background: var(--backdrop);
  }
  .stage {
    position: relative;
    width: 1200px;
    height: 960px;
  }
  .card {
    position: absolute;
    top: 168px;
    width: 361px;
    height: 629px;
    box-shadow: 0 4px 10px rgba(0,0,0,0.25);
    box-sizing: border-box;
    font-family: "Arimo", Arial, sans-serif;
  }
  /* Front: referral promo */
  .card-front {
    left: 205px;
    background: linear-gradient(180deg, var(--red) 0%, #9e2a22 30%, #4a3a22 55%, var(--green) 78%, var(--green-dark) 100%);
    color: var(--white);
    text-align: center;
  }
  .brand-name-front {
    position: absolute;
    top: 30px;
    left: 0;
    right: 0;
    font-family: "Arimo", Arial, sans-serif;
    font-weight: 700;
    font-size: 30px;
    line-height: 1.1;
    color: var(--white);
  }
  .promo {
    position: absolute;
    top: 138px;
    left: 42px;
    width: 276px;
    font-family: "Rubik Dirt", "Arial Black", sans-serif;
  }
  .promo-tag {
    display: block;
    background: var(--white);
    color: var(--red);
    font-size: 29px;
    line-height: 34px;
    text-align: center;
    border-radius: 3px;
  }
  .promo-get {
    display: flex;
    align-items: center;
    justify-content: center;
    margin-top: 6px;
    color: var(--white);
  }
  .promo-get .big { font-size: 86px; line-height: 86px; }
  .promo-get .small {
    font-size: 36px;
    line-height: 36px;
    margin-left: 8px;
    text-align: left;
  }
  .promo-amount {
    display: block;
    font-size: 112px;
    line-height: 112px;
    color: var(--white);
    margin-top: -4px;
  }
  /* Back: contact details */
  .card-back {
    left: 635px;
    background: var(--white);
    text-align: center;
  }
  .brand-name-back {
    position: absolute;
    top: 112px;
    left: 0;
    right: 0;
    display: flex;
    align-items: center;
    justify-content: center;
    gap: 10px;
    font-weight: 700;
    font-size: 27px;
    line-height: 1.15;
    color: var(--green);
  }
  .brand-dot {
    width: 14px;
    height: 14px;
    border-radius: 50%;
    background: var(--red);
    flex: none;
  }
  .person {
    position: absolute;
    top: 296px;
    left: 0;
    right: 0;
  }
  .person-name {
    margin: 0;
    font-size: 24px;
    font-weight: 700;
    color: var(--green);
    letter-spacing: 0.5px;
  }
  .person-title {
    margin: 2px 0 0;
    font-size: 17px;
    color: var(--red);
  }
  .contact-list {
    list-style: none;
    margin: 14px 0 0;
    padding: 0;
    font-size: 17px;
    color: var(--grey-text);
    line-height: 25px;
  }
  .contact-list li {
    display: flex;
    align-items: center;
    justify-content: center;
    gap: 6px;
  }
  .contact-list svg { width: 14px; height: 14px; }
  .divider-dots {
    display: flex;
    justify-content: center;
    align-items: center;
    gap: 9px;
    margin-top: 18px;
  }
  .divider-dots span {
    width: 8px; height: 8px; border-radius: 50%; background: var(--green);
  }
  .divider-dots span.mid { width: 11px; height: 11px; background: var(--red); }
  .address {
    margin: 18px 0 0;
    font-size: 17px;
    line-height: 22px;
    color: var(--grey-text);
    font-style: normal;
  }
  .services {
    margin: 10px 0 0;
    font-size: 14px;
    font-weight: 700;
    color: var(--grey-text);
    line-height: 21px;
  }
  .services .bullet { color: var(--red); font-size: 12px; margin-right: 2px; }
  .services .item + .item { margin-left: 6px; }
</style>
</head>
<body>
<div class="stage">

  <section class="card card-front" aria-label="Card front: referral offer">
    <div class="brand-name-front">Crestline<br>Lending Group</div>
    <div class="promo">
      <span class="promo-tag">REFER A FRIEND</span>
      <div class="promo-get">
        <span class="big">GET</span>
        <span class="small">UP<br>TO</span>
      </div>
      <span class="promo-amount">$100</span>
    </div>
  </section>

  <section class="card card-back" aria-label="Card back: contact details">
    <div class="brand-name-back">
      <span class="brand-dot"></span>
      <span>Crestline<br>Lending Group</span>
    </div>

    <div class="person">
      <p class="person-name">JANE DOE</p>
      <p class="person-title">Branch Manager</p>

      <ul class="contact-list">
        <li>
          <svg viewBox="0 0 16 16" aria-hidden="true"><path fill="#c41f26" d="M3.6 1.5l2.2 2.6-1.3 1.6c.9 2 2.4 3.5 4.4 4.4l1.6-1.3 2.6 2.2-1.4 2.2C6.5 14.8 1.2 9.5 1.4 2.9z"/></svg>
          (505) 555-1212
        </li>
        <li>
          <svg viewBox="0 0 16 16" aria-hidden="true"><rect x="1.5" y="3.5" width="13" height="9" fill="none" stroke="#c41f26" stroke-width="1.4"/><path d="M1.5 3.5l6.5 5 6.5-5" fill="none" stroke="#c41f26" stroke-width="1.4"/></svg>
          jdoe@crestlinelending.com
        </li>
        <li>
          <svg viewBox="0 0 16 16" aria-hidden="true"><g fill="none" stroke="#c41f26" stroke-width="1.2"><circle cx="8" cy="8" r="6.3"/><ellipse cx="8" cy="8" rx="2.8" ry="6.3"/><path d="M1.7 8h12.6M2.8 4.8h10.4M2.8 11.2h10.4"/></g></svg>
          www.crestlinelending.com
        </li>
      </ul>

      <div class="divider-dots" aria-hidden="true"><span></span><span class="mid"></span><span></span></div>

      <address class="address">123 Elm Street<br>Suite B, Anytown, Texas 55555</address>

      <p class="services">
        <span class="item"><span class="bullet">●</span>TITLE LOANS</span><br>
        <span class="item"><span class="bullet">●</span> PERSONAL LOANS</span>
        <span class="item"><span class="bullet">●</span> TAX SERVICES</span>
      </p>
    </div>
  </section>

</div>
</body>
</html>
```